Amber Lantern Cafe Business Card

We need a business card design for a new European Cafe. Main menu will be coffee and deserts.

Requirements
Must have
• Logo - 1 of the attached versions
Address - TBA (you can use 487 Morrow Ave Unit 9 for now)
Phone - TBA (you can use 555-238-4176 for now)

```html
<!DOCTYPE html>
<html lang="en">
<head>
<meta charset="utf-8">
<title>Amber Lantern Cafe Business Card</title>
<link rel="stylesheet" href="https://fonts.googleapis.com/css2?family=Open+Sans:wght@400;600&family=Arimo:wght@400;700&display=swap">
<style>
  :root {
    --page: #ffffff;
    --card: #3c2214;
    --pattern-light: #5a2e18;
    --pattern-dark: #3c2214;
    --band: #5c3312;
    --ink: #0d0806;
    --name: #f1dcc0;
    --mark: #000000;
  }
  html, body {
    margin: 0;
    padding: 0;
    width: 1200px;
    height: 1200px;
    overflow: hidden;
    background: var(--page);
  }
  .canvas {
    position: relative;
    width: 1200px;
    height: 1200px;
  }
  .business-card {
    position: absolute;
    left: 83px;
    top: 255px;
    width: 1035px;
    height: 593px;
    border-radius: 45px;
    background: var(--card);
    overflow: hidden;
  }
  .card-pattern {
    position: absolute;
    inset: 0;
    width: 100%;
    height: 100%;
  }
  .brand-square {
    position: absolute;
    left: 409px;
    top: 48px;
    width: 216px;
    height: 215px;
    border-radius: 12px;
    background: var(--mark);
  }
  .brand-name {
    position: absolute;
    left: 0;
    right: 0;
    top: 300px;
    margin: 0;
    text-align: center;
    font-family: "Open Sans", sans-serif;
    font-weight: 400;
    color: var(--name);
  }
  .brand-name-main {
    display: block;
    font-size: 74px;
    line-height: 1;
    letter-spacing: -1.5px;
  }
  .brand-name-sub {
    display: block;
    margin-top: 12px;
    font-size: 46px;
    line-height: 1;
    letter-spacing: 4px;
  }
  .contact-band {
    position: absolute;
    left: 0;
    right: 0;
    top: 447px;
    height: 96px;
    background: var(--band);
    display: flex;
    align-items: center;
    padding-left: 67px;
    gap: 38px;
    font-family: "Arimo", sans-serif;
    font-size: 39px;
    color: var(--ink);
  }
  .contact-item { white-space: nowrap; }
  .contact-label { font-weight: 700; }
</style>
</head>
<body>
<main class="canvas">
  <section class="business-card">
    <svg class="card-pattern" viewBox="0 0 1035 593" preserveAspectRatio="none"
         role="img" aria-label="Faint repeating pattern of coffee cup emblems across the card background">
      <defs>
        <radialGradient id="pattern-glow" cx="50%" cy="45%" r="70%">
          <stop offset="0%" stop-color="#5a2e18" stop-opacity="0.55"/>
          <stop offset="100%" stop-color="#3c2214" stop-opacity="0"/>
        </radialGradient>
      </defs>
      <rect x="0" y="0" width="1035" height="593" fill="url(#pattern-glow)"/>
    </svg>

    <div class="brand-square"></div>
    <h1 class="brand-name">
      <span class="brand-name-main">Amber Lantern</span>
      <span class="brand-name-sub">Cafe</span>
    </h1>

    <div class="contact-band">
      <span class="contact-item"><span class="contact-label">A</span>:487 Morrow Ave Unit 9</span>
      <span class="contact-item"><span class="contact-label">P</span>:555-238-4176</span>
    </div>
  </section>
</main>
</body>
</html>
```